CD-Cover-Design für Musikerin
Zielgruppe
Ich bin Musikerin und gebe Seminare. Zielgruppe sind alle die zu meinen Konzerten und Seminaren kommen.
Aufgabenstellung
künstlerisch und kreativ, verspielt

```html
<!DOCTYPE html>
<html lang="en">
<head>
<meta charset="utf-8">
<title>Solace – CD Cover</title>
<link href="https://fonts.googleapis.com/css2?family=Open+Sans:wght@400;600&family=Signika:wght@600&family=Great+Vibes&family=Dancing+Script:wght@700&display=swap" rel="stylesheet">
<style>
  :root{
    --magenta:#a3157e;
    --violet:#6c0c9e;
    --orange:#f07a1a;
    --amber:#f7b52a;
    --red-orange:#e6421c;
    --white:#ffffff;
    --track-purple:#8a16a8;
    --gold:#f5a623;
  }
  html,body{margin:0;padding:0;width:1200px;height:619px;overflow:hidden;background:var(--white);}
  .canvas{position:relative;width:1200px;height:619px;overflow:hidden;font-family:"Open Sans",sans-serif;}
  .panel{position:absolute;top:21px;height:576px;overflow:hidden;
    background:linear-gradient(90deg,var(--magenta) 0%,#951088 55%,var(--violet) 100%);}
  .panel--back{left:23px;width:577px;}
  .panel--front{left:601px;width:576px;}

  .mandala{position:absolute;border-radius:50%;
    background:radial-gradient(circle,var(--amber) 45%,var(--orange) 70%,var(--red-orange) 100%);}
  .mandala--back{left:116px;top:78px;width:362px;height:362px;}
  .mandala--front{left:65px;top:38px;width:458px;height:458px;}

  .tracklist-disc{position:absolute;left:204px;top:166px;width:186px;height:186px;border-radius:50%;background:var(--white);}
  .tracklist{position:absolute;left:204px;top:194px;width:186px;margin:0;padding:0;list-style:none;text-align:center;
    font-family:"Signika",sans-serif;font-weight:600;font-size:13.5px;line-height:15.7px;color:var(--track-purple);}
  .tracklist .num{color:var(--orange);}

  .manifesto{position:absolute;left:0;top:13px;width:560px;text-align:center;margin:0;
    color:var(--white);font-size:13.2px;line-height:17px;}
  .signature{position:absolute;left:397px;top:66px;margin:0;color:var(--white);
    font-family:"Dancing Script",cursive;font-size:23px;}

  .portrait{position:absolute;background:linear-gradient(180deg,#8a5a4a,#2a1a1a 45%,#1a1010);}
  .portrait--violinist{left:0;top:232px;width:175px;height:344px;border-radius:80px 90px 0 0;}
  .portrait--singer{left:117px;top:90px;width:352px;height:352px;border-radius:50%;
    border:2px solid #c8a020;box-sizing:border-box;
    background:radial-gradient(circle at 50% 45%,#c98a6a 0%,#8a4a2a 35%,#3f6a2a 70%,#2a4a1e 100%);}

  .contact{position:absolute;left:164px;top:463px;width:400px;text-align:center;margin:0;
    color:var(--white);font-size:10.5px;line-height:13px;}
  .contact .link{color:var(--gold);font-weight:600;}
  .credits{position:absolute;left:134px;top:496px;width:450px;text-align:center;margin:0;
    color:var(--white);font-size:8.8px;line-height:11.8px;}
  .credits .hl{color:var(--gold);}

  .title{position:absolute;left:40px;top:330px;margin:0;color:var(--white);
    font-family:"Great Vibes",cursive;font-weight:400;font-size:175px;line-height:1;letter-spacing:-3px;}
</style>
</head>
<body>
<div class="canvas">
  <section class="panel panel--back">
    <p class="manifesto">Music is our means of transport and a direct communication with our essence.<br>We would like to take you there with our music. Communicating THIS is our joy.<br>We thank you and enjoy...Our music is inspired by the spirit of Oneness.</p>
    <p class="signature">Lorina und Kaito</p>

    <div class="mandala mandala--back" role="img" aria-label="Orange mandala ornament framing the track list"></div>
    <div class="tracklist-disc"></div>
    <ol class="tracklist">
      <li><span class="num">1.</span> Ouvrir le cœur</li>
      <li><span class="num">2.</span> Sat Nam Om</li>
      <li><span class="num">3.</span> Wonders</li>
      <li><span class="num">4.</span> Leuchtende Stille</li>
      <li><span class="num">5.</span> Solace</li>
      <li><span class="num">6.</span> Anahata</li>
      <li><span class="num">7.</span> Wir sind Licht</li>
      <li><span class="num">8.</span> Beyond the Sky</li>
    </ol>

    <div class="portrait portrait--violinist" role="img" aria-label="Photo of the violinist holding his violin and bow"></div>

    <p class="contact">Feel free to contact us. Booking, concerts and contact on our website:<br>
      <span class="link">http://www.LorinaandKaito.com</span> / <span class="link">Mail: lorina@lorinamusik.example</span></p>
    <p class="credits">All song written by Lorina Lindqvist-Maren.<br>
      All tracks performed by Lorina on vocals, guitar and harmonium and Kaito-Wen Lu on his celestial violin.<br>
      Special thanks to: Tomas Rell for his backing vocals on tracks<br>
      <span class="hl">7 &amp; 8</span> and his sarot/sisa performance on track <span class="hl">8.</span> Jonas Ebbert playing the guitar on tracks<br>
      <span class="hl">4 &amp; 7.</span> / Marco Sévan playing the cajon on tracks <span class="hl">1 &amp; 3.</span> Pierre Kollen @ Halbton Studios for<br>
      recording and mixdown <span class="hl">KMV all rights reserved Lorina Lindqvist-Maren</span></p>
  </section>

  <section class="panel panel--front">
    <div class="mandala mandala--front" role="img" aria-label="Orange mandala ornament around the portrait"></div>
    <div class="portrait portrait--singer" role="img" aria-label="Portrait photo of the singer with a flower crown in a garden"></div>
    <h1 class="title">Solace</h1>
  </section>
</div>
</body>
</html>
```